Indie author needs a minimalist book cover

I need a book cover for my latest book on personal finance and investing. The book is called, "The Quiet Harvest: Methods for Steady Savings, Careful Spending, and a Calm Future". This is volume one of a three part series on the FI/RE movement, which stands for 'Financial Independence/Retire Early'. This book is on the foundational principles of FI/RE and details the specific steps that these 'Quiet Harvest' involved in this community have done to position themselves to retire from paid work and live the life of their dreams - many only in their 20's, 30's and early 40's.

Title: The Quiet Harvest
Author: PK Brenner
Volume 1: Foundations
Book dimensions: 6"x9"

Book Blurb (for back cover):

Let's face it, no one wants to be different. But sometimes following the 'normal' crowd gets you no further than that crowd.

When it comes to money, the normal crowd is your typical consumer. Deep in debt, struggling to make ends meet, but still spending money on the newest 'thing' that just came out.

But there's another group that's been forming - right on the fringes of the personal finance world. I call them The Quiet Harvest. This book is about these superheroes of personal finance.

In it, you will learn:
• Who The Quiet Harvest are and what is this FI/RE Movement they are apart of
• What basic strategy they use to control their money
• How they became debt-free - and how you can join them
• How to use the SP/CE Lever to help you really move the needle towards financial independence
• How to diversify your income with a side-hustle and which one to choose
• The quiet harvest savings plan that will allow you to reach financial independence in ten years or less

This first book in The Quiet Harvest series is about building a solid foundation so you and your family can become Quiet Harvest, reach financial freedom, retire early, and live a rich life.

Target Market(s)

Individuals looking to take control of their money, reach financial independence, and retire early.

Font styles to use
Sans Serif
Other font styles liked:
• Arvo

Colors

Designer to choose colors to be used in the design.

Requirements
Must have
• A minimalist design (see examples), the title of the book, my author name, and the volume number and name (see below).
• My vision for the cover is to have a way to represent an 'outlier' in a simple, minimalistic way. I'm not set on any specific design - I'm open to what the designers come up with; I don't want to hold back anyone's creativity.
• Title: The Quiet Harvest
• Author: PK Brenner
• Volume 1: Foundations
• Book Blurb (for back cover):
• Let's face it, no one wants to be different. But sometimes following the 'normal' crowd gets you no further than that crowd.
• When it comes to money, the normal crowd is your typical consumer. Deep in debt, struggling to make ends meet, but still spending money on the newest 'thing' that just came out.
• But there's another group that's been forming - right on the fringes of the personal finance world. I call them The Quiet Harvest. This book is about these superheroes of personal finance.
• In it, you will learn:
• • Who The Quiet Harvest are and what is this FI/RE Movement they are apart of
• • What basic strategy they use to control their money
• • How they became debt-free - and how you can join them
• • How to use the SP/CE Lever to help you really move the needle towards financial independence
• • How to diversify your income with a side-hustle and which one to choose
• • The quiet harvest savings plan that will allow you to reach financial independence in ten years or less
• This first book in The Quiet Harvest series is about building a solid foundation so you and your family can become Quiet Harvest, reach financial freedom, retire early, and live a rich life.
Nice to have
• The subtitle - but only if it's not too crowded. Like I said before, I'm more interested in maintaining a minimalist aesthetic.
• The subtitle is: "Methods for Steady Savings, Careful Spending, And A Calm Future"
Should not have
• Too many colors or objects on the cover.

```html
<!DOCTYPE html>
<html lang="en">
<head>
<meta charset="utf-8">
<title>The Quiet Harvest – Cover Wrap</title>
<link href="https://fonts.googleapis.com/css2?family=Montserrat:wght@400;600;700&family=Arimo:wght@400;700&family=Barlow:wght@700&display=swap" rel="stylesheet">
<style>
  :root {
    --paper: #ffffff;
    --trim: #c9c9c9;
    --blue: #2f7fc1;
    --orange: #fbb040;
    --ink: #1a1a1a;
    --grey: #4a4a4a;
  }
  * { margin: 0; padding: 0; box-sizing: border-box; }
  html, body { width: 1200px; height: 853px; overflow: hidden; background: var(--paper); }
  .wrap { position: relative; width: 1200px; height: 853px; background: var(--paper); }

  .trim-line { position: absolute; background: var(--trim); }
  .trim-top { left: 0; right: 0; top: 10px; height: 1px; }
  .trim-bottom { left: 0; right: 0; top: 842px; height: 1px; }
  .trim-left { top: 0; bottom: 0; left: 10px; width: 1px; }
  .trim-right { top: 0; bottom: 0; left: 1190px; width: 1px; }
  .trim-spine-l { top: 0; bottom: 0; left: 566px; width: 1px; }
  .trim-spine-r { top: 0; bottom: 0; left: 634px; width: 1px; }

  /* Back cover */
  .back-copy {
    position: absolute; left: 66px; top: 50px; width: 444px;
    font-family: "Montserrat", sans-serif; font-size: 14.2px; line-height: 16.8px;
    color: var(--ink); text-align: justify;
  }
  .back-copy p { margin-bottom: 9px; }
  .back-copy .learn-head { font-weight: 600; margin-bottom: 4px; }
  .learn-list { list-style: none; margin-bottom: 9px; text-align: left; }
  .learn-list li { position: relative; padding-left: 29px; margin-bottom: 4px; padding-right: 30px; }
  .learn-list li::before { content: "•"; position: absolute; left: 3px; top: 0; font-size: 16px; }

  /* Spine */
  .spine {
    position: absolute; left: 566px; top: 10px; width: 68px; height: 832px;
    background: var(--blue); color: var(--paper);
  }
  .spine-text {
    position: absolute; left: 50%; writing-mode: vertical-rl;
    transform: translateX(-50%); white-space: nowrap; line-height: 1;
  }
  .spine-title { top: 60px; font-family: "Montserrat", sans-serif; font-weight: 700; font-size: 28px; letter-spacing: 3px; }
  .spine-author { top: 560px; font-family: "Arimo", sans-serif; font-weight: 400; font-size: 29px; letter-spacing: 0.5px; }

  /* Front cover */
  .front { position: absolute; left: 634px; top: 10px; width: 556px; height: 832px; overflow: hidden; }
  .subtitle {
    position: absolute; left: 0; width: 556px; top: 40px; text-align: center;
    font-family: "Arimo", sans-serif; font-weight: 400; font-size: 21.5px; line-height: 26px;
    letter-spacing: 0.9px; color: var(--blue); text-transform: uppercase;
  }
  .volume {
    position: absolute; left: 0; width: 556px; top: 99px; text-align: center;
    font-family: "Arimo", sans-serif; font-size: 17px; letter-spacing: 2.2px; color: var(--grey);
  }
  .cover-title { font-weight: 400; }
  .title-top {
    position: absolute; left: 48px; width: 464px; top: 222px;
    font-family: "Arimo", sans-serif; font-weight: 400; font-size: 52px; line-height: 1;
    color: var(--blue); display: flex; justify-content: space-between;
  }
  .title-main {
    position: absolute; left: 48px; width: 464px; top: 263px; text-align: center;
    font-family: "Barlow", sans-serif; font-weight: 700; font-size: 104px; line-height: 1;
    letter-spacing: 1px; color: var(--orange);
  }
  .author-front {
    position: absolute; left: 0; width: 556px; top: 772px; text-align: center;
    font-family: "Arimo", sans-serif; font-size: 38px; letter-spacing: 1.5px; color: var(--blue);
  }
  .marble-lone, .marble-crowd { position: absolute; }
  .marble-lone { left: 148px; top: 446px; width: 64px; height: 64px; }
  .marble-crowd { left: 286px; top: 550px; width: 270px; height: 282px; }
</style>
</head>
<body>
<div class="wrap">
  <div class="trim-line trim-top"></div>
  <div class="trim-line trim-bottom"></div>
  <div class="trim-line trim-left"></div>
  <div class="trim-line trim-right"></div>
  <div class="trim-line trim-spine-l"></div>
  <div class="trim-line trim-spine-r"></div>

  <section class="back-copy">
    <p>Let's face it, no one wants to be different. But sometimes following the 'normal' crowd gets you no further than that crowd.</p>
    <p>When it comes to money, the normal crowd is your typical consumer. Deep in debt, struggling to make ends meet, but still spending money on the newest 'thing' that just came out.</p>
    <p>But there's another group that's been forming - right on the fringes of the personal finance world. I call them The Quiet Harvest. This book is about these superheroes of personal finance.</p>
    <p class="learn-head">In it, you will learn:</p>
    <ul class="learn-list">
      <li>Who The Quiet Harvest are and what is this FI/RE Movement they are apart of</li>
      <li>What basic strategy they use to control their money</li>
      <li>How they became debt-free - and how you can join them</li>
      <li>How to use the SP/CE Lever to help you really move the needle towards financial independence</li>
      <li>How to diversify your income with a side-hustle and which one to choose</li>
      <li>The quiet harvest savings plan that will allow you to reach financial independence in ten years or less</li>
    </ul>
    <p>This first book in The Quiet Harvest series is about building a solid foundation so you and your family can become Quiet Harvest, reach financial freedom, retire early, and live a rich life.</p>
  </section>

  <aside class="spine">
    <span class="spine-text spine-title">THE QUIET HARVEST</span>
    <span class="spine-text spine-author">PK BRENNER</span>
  </aside>

  <section class="front">
    <h2 class="subtitle">Methods for Steady Savings,<br>Careful Spending, and a Calm Future</h2>
    <p class="volume">VOLUME 1: FOUNDATIONS</p>
    <h1 class="cover-title">
      <span class="title-top"><span>T</span><span>H</span><span>E</span><span>&nbsp;</span><span>Q</span><span>U</span><span>I</span><span>E</span><span>T</span></span>
      <span class="title-main">HARVEST</span>
    </h1>

    <svg class="marble-lone" viewBox="0 0 64 64" role="img" aria-label="Photo of a single orange glass marble set apart">
      <defs>
        <radialGradient id="loneGlow" cx="40%" cy="40%" r="60%">
          <stop offset="0" stop-color="#ffd98a"/>
          <stop offset="1" stop-color="#f4a52a"/>
        </radialGradient>
      </defs>
      <circle cx="30" cy="30" r="29" fill="url(#loneGlow)"/>
    </svg>

    <svg class="marble-crowd" viewBox="0 0 270 282" role="img" aria-label="Photo of a cluster of blue glass marbles in the corner">
      <defs>
        <radialGradient id="crowdGlow" cx="75%" cy="75%" r="80%">
          <stop offset="0" stop-color="#1f6fc4"/>
          <stop offset="0.6" stop-color="#5aa2e3" stop-opacity="0.85"/>
          <stop offset="1" stop-color="#ffffff" stop-opacity="0"/>
        </radialGradient>
      </defs>
      <rect width="270" height="282" fill="url(#crowdGlow)"/>
    </svg>

    <p class="author-front">PK BRENNER</p>
  </section>
</div>
</body>
</html>
```